Design The Loomfield Hompage

See powerpoint

Industry/Entity Type

SAAS data product

Coding

Coded - Design and coding required

Number of Pages Required

4 page

Font styles to use
Sans Serif

```html
<!DOCTYPE html>
<html lang="en">
<head>
<meta charset="utf-8">
<title>The Loomfield – Public Data Made Easy</title>
<link href="https://fonts.googleapis.com/css2?family=Poppins:wght@300;400;500;600;700&display=swap" rel="stylesheet">
<style>
:root{
  --ink:#3f4d63;
  --ink-soft:#56627a;
  --yellow:#e9b816;
  --blue:#2f5aa8;
  --blue-mid:#6f95d8;
  --blue-light:#dfe8fb;
  --line:#e3e6ec;
  --footer:#45536a;
  --white:#ffffff;
}
*{box-sizing:border-box;margin:0;padding:0}
html,body{width:756px;height:1200px;overflow:hidden;background:var(--white)}
body{font-family:'Poppins',sans-serif;color:var(--ink);position:relative}
.abs{position:absolute}

/* header */
.brand{left:56px;top:30px;display:flex;align-items:center;gap:6px}
.brand-dot{width:14px;height:14px;border-radius:50%;background:var(--blue)}
.brand-name{font-size:15px;font-weight:600;color:var(--ink)}
.nav{left:308px;top:16px;display:flex;align-items:center;gap:21px;font-size:8.5px;font-weight:500;letter-spacing:.2px}
.nav a{color:var(--ink);text-decoration:none}
.btn{display:inline-flex;align-items:center;justify-content:center;border-radius:15px;font-size:8.5px;font-weight:600;height:28px;text-decoration:none}
.btn-fill{background:var(--yellow);color:var(--white)}
.btn-line{border:1.2px solid var(--ink);color:var(--ink)}
.nav .btn-fill{width:71px}
.nav .btn-line{width:71px;margin-left:-16px}
.header-rule{left:196px;top:61px;width:560px;height:1px;background:var(--line)}

/* hero */
.hero-title{left:55px;top:124px;font-size:41px;line-height:45px;font-weight:700;color:var(--ink)}
.hero-copy{left:57px;top:230px;width:272px;font-size:8.8px;line-height:14px;font-weight:300;color:var(--ink-soft)}
.hero-copy p+p{margin-top:9px}
.hero-actions{left:58px;top:324px;display:flex;gap:7px}
.hero-actions .btn-fill{width:166px}
.hero-actions .btn-line{width:71px}
.hero-art{left:340px;top:76px;width:392px;height:364px;
  background:
    radial-gradient(ellipse 34% 30% at 60% 44%,#3563b8 0%,#4a78c8 45%,rgba(111,149,216,0) 100%),
    radial-gradient(ellipse 52% 48% at 58% 48%,rgba(111,149,216,.55) 0%,rgba(223,232,251,.9) 55%,rgba(255,255,255,0) 100%);}

/* developers */
.dev-title{left:60px;top:472px;font-size:22.5px;line-height:31px;font-weight:700}
.dev-copy{left:61px;top:541px;width:350px;font-size:8px;line-height:14px;font-weight:300;color:var(--ink-soft)}
.dev-art{left:50px;top:580px;width:380px;height:300px;
  background:
    radial-gradient(ellipse 30% 24% at 52% 48%,#2f5aa8 0%,#4a78c8 50%,rgba(111,149,216,0) 100%),
    radial-gradient(ellipse 52% 46% at 50% 50%,rgba(111,149,216,.5) 0%,rgba(223,232,251,.85) 55%,rgba(255,255,255,0) 100%);}

.features{left:456px;top:480px;width:246px}
.feature{position:absolute;left:0;width:246px}
.feature svg{position:absolute;left:2px;top:0}
.feature h3{position:absolute;left:48px;font-size:12px;font-weight:700;color:var(--ink)}
.feature p{position:absolute;left:49px;top:22px;width:200px;font-size:8.4px;line-height:14px;font-weight:300;color:var(--ink-soft)}
.feature .rule{position:absolute;left:48px;width:195px;height:1px;background:var(--line)}

/* footer */
.footer-shape{left:0;top:858px}
.foot-brand{left:76px;top:1000px;display:flex;align-items:center;gap:6px}
.foot-brand .brand-dot{background:#8fb1f0}
.foot-brand .brand-name{color:var(--white);font-size:15px}
.foot-about{left:76px;top:1076px;width:180px;font-size:8.5px;line-height:14px;font-weight:300;color:var(--white)}
.foot-col{top:996px;color:var(--white)}
.foot-col h4{font-size:12px;font-weight:600;margin-bottom:12px}
.foot-col ul{list-style:none;font-size:8.5px;font-weight:300;line-height:16.8px}
.contact-line{display:flex;gap:8px;font-size:8.5px;font-weight:300;line-height:12px}
.socials{display:flex;gap:4px;margin-top:12px}
.socials span{width:24px;height:24px;border-radius:50%;background:#5a6880}
.foot-rule{left:56px;top:1159px;width:644px;height:1px;background:#65738a}
.copyright{left:0;width:756px;top:1173px;text-align:center;font-size:8.5px;color:var(--white)}
.to-top{left:716px;top:1148px;width:25px;height:25px;border-radius:50%;background:var(--yellow);display:flex;align-items:center;justify-content:center}
</style>
</head>
<body>

<header>
  <div class="abs brand"><span class="brand-dot"></span><span class="brand-name">The Loomfield</span></div>
  <nav class="abs nav">
    <a href="#">PRICING</a><a href="#">DOCUMENTATION</a><a href="#">DATA</a><a href="#">BLOG</a>
    <a href="#" class="btn btn-fill">SIGNUP</a>
    <a href="#" class="btn btn-line">LOGIN</a>
  </nav>
  <div class="abs header-rule"></div>
</header>

<section>
  <h1 class="abs hero-title">Public Data<br>Made Easy</h1>
  <div class="abs hero-copy">
    <p>From demographics to economics, from weather to health, on country level or community level. The Loomfield collects many public data sources and organizes it for you.</p>
    <p>Use The Loomfield API or SDK to easily get public data from many different sources.</p>
  </div>
  <div class="abs hero-actions">
    <a class="btn btn-fill">REGISTER AND START FOR FREE</a>
    <a class="btn btn-line">PRICING</a>
  </div>
  <div class="abs hero-art" role="img" aria-label="Illustration of two people working with a large data dashboard showing charts"></div>
</section>

<section>
  <h2 class="abs dev-title">Designed for Developers<br>In Need of Data</h2>
  <p class="abs dev-copy">As a data scientist or engineer you always are looking for getting more data in with more efficiency. This is exactly what The Loomfield is making possible for you.</p>
  <div class="abs dev-art" role="img" aria-label="Illustration of two people beside a large video player and data charts"></div>

  <div class="abs features">
    <div class="feature" style="top:4px">
      <svg width="32" height="32" viewBox="0 0 32 32" fill="none" stroke="#3a6fd8" stroke-width="1.2"><rect x="1" y="2" width="26" height="22" rx="2"/><line x1="5" y1="14" x2="18" y2="14"/><line x1="5" y1="18" x2="14" y2="18"/><circle cx="25" cy="25" r="5"/></svg>
      <h3 style="top:6px">Many Sources</h3><div class="rule" style="top:39px"></div>
    </div>
    <div class="feature" style="top:54px">
      <svg width="32" height="34" viewBox="0 0 32 34" fill="none" stroke="#3a6fd8" stroke-width="1.2"><rect x="3" y="8" width="26" height="20" rx="2"/><circle cx="16" cy="17" r="5"/><line x1="10" y1="32" x2="22" y2="32"/></svg>
      <h3 style="top:7px">Integrate</h3><div class="rule" style="top:43px"></div>
    </div>
    <div class="feature" style="top:116px">
      <svg width="32" height="34" viewBox="0 0 32 34" fill="none" stroke="#3a6fd8" stroke-width="1.2"><circle cx="15" cy="18" r="14"/><path d="M26 2a4 4 0 0 1 4 4c0 3-4 7-4 7s-4-4-4-7a4 4 0 0 1 4-4z"/></svg>
      <h3 style="top:0">Regional</h3>
      <p>Do you need regional information in your pipeline ? The Loomfield provides public data up to community level.</p>
      <div class="rule" style="top:77px"></div>
    </div>
    <div class="feature" style="top:197px">
      <svg width="34" height="34" viewBox="0 0 34 34" fill="none" stroke="#3a6fd8" stroke-width="1.2"><rect x="7" y="7" width="20" height="20" rx="2"/><circle cx="17" cy="17" r="5"/><line x1="17" y1="1" x2="17" y2="7"/><line x1="17" y1="27" x2="17" y2="33"/><line x1="1" y1="17" x2="7" y2="17"/><line x1="27" y1="17" x2="33" y2="17"/></svg>
      <h3 style="top:7px">Automate</h3><div class="rule" style="top:43px"></div>
    </div>
    <div class="feature" style="top:250px">
      <svg width="34" height="34" viewBox="0 0 34 34" fill="none" stroke="#3a6fd8" stroke-width="1.2"><path d="M3 12l14-6 14 6-14 6z"/><path d="M3 12v14l14 6 14-6V12"/><line x1="17" y1="18" x2="17" y2="32"/></svg>
      <h3 style="top:7px">The Loomfield SDK</h3><div class="rule" style="top:44px"></div>
    </div>
    <div class="feature" style="top:304px">
      <svg width="32" height="34" viewBox="0 0 32 34" fill="none" stroke="#3a6fd8" stroke-width="1.2"><rect x="4" y="2" width="18" height="22" rx="2"/><line x1="8" y1="8" x2="18" y2="8"/><line x1="8" y1="12" x2="16" y2="12"/><circle cx="16" cy="22" r="6"/><line x1="20" y1="27" x2="27" y2="33"/></svg>
      <h3 style="top:8px">Tracable</h3>
    </div>
  </div>
</section>

<footer>
  <svg class="abs footer-shape" width="756" height="342" viewBox="0 0 756 342">
    <defs><linearGradient id="footFill" x1="0" y1="1" x2="0.4" y2="0"><stop offset="0" stop-color="#5f7089"/><stop offset="0.5" stop-color="#45536a"/></linearGradient></defs>
    <ellipse cx="202" cy="83" rx="104" ry="35" fill="#f5e6b3"/>
    <path d="M0 28C70 85 140 110 220 98 340 80 420 20 560 6 650-3 720 20 756 48V342H0Z" fill="url(#footFill)"/>
  </svg>

  <div class="abs foot-brand"><span class="brand-dot"></span><span class="brand-name">The Loomfield</span></div>
  <p class="abs foot-about">The Loomfield was created to simplify access to public data and save you countless hours of manual collection</p>

  <div class="abs foot-col" style="left:274px">
    <h4>Our Product</h4>
    <ul><li>Introduction</li><li>The datamodels</li><li>The API</li><li>The SDK</li></ul>
  </div>
  <div class="abs foot-col" style="left:404px">
    <h4>The Company</h4>
    <ul><li>About</li><li>Frequently Asked Questions</li><li>Privacy Policy</li><li>Cookie Policy</li><li>Terms of Service</li></ul>
  </div>
  <div class="abs foot-col" style="left:562px">
    <h4>Contact Us</h4>
    <div class="contact-line">
      <svg width="11" height="9" viewBox="0 0 11 9" style="margin-top:2px"><rect width="11" height="9" rx="1" fill="#e9b816"/><path d="M0.5 1l5 4 5-4" stroke="#45536a" fill="none"/></svg>
      <span>Email:<br>hello@loomfield-mail.io</span>
    </div>
    <div class="socials" aria-label="Social links"><span></span><span></span></div>
  </div>

  <div class="abs foot-rule"></div>
  <p class="abs copyright">© 2024 The Loomfield. All rights reserved.</p>
  <div class="abs to-top"><svg width="8" height="5" viewBox="0 0 8 5"><path d="M1 4l3-3 3 3" stroke="#fff" fill="none" stroke-width="1.2"/></svg></div>
</footer>

</body>
</html>
```